Weather of the Heart Is the Ledger A Novel by Carl Whitby and Martin Holloway

Weather of the Heart Is the Ledger is a business novel about leadership, follower-ship, resilience, and insight.
It follows a high-performing executive whose conventional management tools and techniques stop working during a professional crisis. His transformation does not come from new strategies or tactics, but from a fundamentally different understanding of how mindset shapes performance, decision-making, leadership and follower-ship. Through the course of the book, the executive, his team, and his customers realize that “State of Mind” (healthy psychological functioning) is the horsepower that drives business and life.
This is not a self-help book, textbook, or memoir. It is thoughtful business fiction with philosophical depth.

Introduction/Preface for the novel:
We wrote this book because something profound changed the way we live, work, and lead. Over the course of several decades - across boardrooms, high-stakes corporate challenges, private practice, and moments of quiet personal insight - we began to see a deeper truth about the human experience. It was a truth that, once seen, dramatically improved the quality of our lives, and the lives of the people with whom we worked.
That truth comes from understanding the Three Principles of Mind, Consciousness, and Thought, as discovered and first articulated by the philosopher and theosopher, Edwin Thorley. Though simple, these Principles point to something universally powerful—how all people experience life from the inside out. When understood, they reveal a level of clarity, resilience, and well-being that can transform not only individuals, but entire organizations.
At first, we tried to write a traditional business book—a primer designed to share how understanding the Principles can lead to more grounded, wise, and effective leadership—without the need for techniques or tools. But as we wrote, we found ourselves returning again and again to stories. Real stories. Composite stories. Fictional ones. We realized that the best way to share this understanding wasn’t through frameworks or prescriptive advice. It was through story.
So, we created one big story.
This novel is the result. Though fictional, it is inspired by real patterns, real shifts, and real struggles we’ve lived through and witnessed over decades of work, together and separately. The characters are inventions, but their experiences are familiar. We’ve watched people just like them transform—from confusion to clarity, from fear to resilience, from burnout to wisdom.
Our hope is that this book moves you—not just as a story, but as an experience. We believe that the ideas woven into Owen Castell’s journey can help anyone live with greater ease, purpose, and peace of mind. Whether you lead a Fortune 500 company or a family of five, what’s offered here is for you.
And if something in this story helps you see your own life with fresh eyes, then the book has done its job.
Welcome to the journey.
—Carl & Martin

Target Market(s)

• Senior leaders, executives, and high-potential managers • Business professionals experiencing pressure, burnout, or diminishing returns from traditional leadership approaches • Leadership coaches and organizational consultants • Readers of intelligent, reflective business fiction or non-business people who are interested in what makes people tick — and achieve their highest potential Tone should appeal to serious, experienced professionals, not beginners or hype-seekers.

Industry/Entity Type

• Business / Leadership / Psychology • Business Fiction • Leadership Novel

Font styles to use
Serif

Colors
0054AA
0677BA
7BADD7
CADEEF
E8F1F8

Requirements
Must have
• We are looking for metaphorical representations of: • A fork in the road • A deviation from the conventional path (that makes all the difference) • One element choosing a different direction—not running away, not rebelling, just seeing differently Think quiet insight, not drama. Must-Haves • Clear, legible title at thumbnail size • A visual metaphor for choice or alternate thinking • Professional, credible aesthetic • Obvious that this is fiction (a novel), not a textbook • Clean typography (no clutter)
Nice to have
• • A sense of motion or transition • Minimalist or restrained color palette • One accent element that signifies insight or departure from convention • Timeless design (should still feel current in 5 or 10 years)
Should not have
• • Literal business clichés (gears, ladders, chess pieces, lightbulbs, compasses, eagles) • Stock-photo people in suits • “Hero CEO” imagery • Overly mystical or “woo-woo” visuals • Aggressive, macho, or hustle-culture tone • Anything cartoonish or silly

```html
<!DOCTYPE html>
<html lang="en">
<head>
<meta charset="utf-8">
<title>Weather of the Heart Is the Ledger — Book Cover</title>
<link rel="stylesheet" href="https://fonts.googleapis.com/css2?family=Playfair+Display:wght@700;800;900&display=swap">
<style>
  :root {
    --page-bg: #f4f4f4;
    --cover-bg: #e8f1f8;
    --ink: #0b2748;
    --blue-deep: #0054aa;
    --blue-mid: #0677ba;
    --blue-soft: #7badd7;
    --blue-pale: #cadeef;
    --blue-mist: #e8f1f8;
  }
  * { margin: 0; padding: 0; box-sizing: border-box; }
  html, body {
    width: 1198px;
    height: 1200px;
    overflow: hidden;
    background: var(--page-bg);
  }
  .book-cover {
    position: absolute;
    left: 250px;
    top: 76px;
    width: 697px;
    height: 1048px;
    background: var(--cover-bg);
    font-family: "Playfair Display", Georgia, serif;
    text-align: center;
  }
  .title {
    position: absolute;
    top: 70px;
    left: 0;
    width: 100%;
    font-weight: 900;
    font-size: 78px;
    line-height: 90px;
    letter-spacing: 0;
    text-transform: uppercase;
  }
  .title-line { display: block; color: var(--ink); }
  .title-line--accent { color: var(--blue-mid); }
  .cover-art {
    position: absolute;
    left: 78px;
    top: 478px;
    width: 540px;
    height: 340px;
  }
  .subtitle {
    position: absolute;
    top: 852px;
    left: 0;
    width: 100%;
    color: var(--blue-deep);
    font-weight: 700;
    font-size: 24px;
    line-height: 34px;
    letter-spacing: 2px;
    text-transform: uppercase;
  }
  .authors {
    position: absolute;
    top: 976px;
    left: 0;
    width: 100%;
    font-weight: 800;
    font-size: 26px;
    color: var(--ink);
  }
  .authors .conjunction { color: var(--blue-mid); font-weight: 700; }
</style>
</head>
<body>
  <main class="book-cover">
    <h1 class="title">
      <span class="title-line">Weather</span>
      <span class="title-line">of the Heart</span>
      <span class="title-line">Is the</span>
      <span class="title-line title-line--accent">Ledger</span>
    </h1>

    <svg class="cover-art" viewBox="0 0 540 340" aria-hidden="true">
      <line class="horizon" x1="20" y1="60" x2="520" y2="60" stroke="var(--blue-soft)" stroke-width="1"/>
      <!-- straight conventional road -->
      <polygon class="road-main" points="190,340 350,340 276,60 264,60" fill="var(--blue-pale)"/>
      <line class="road-main-centre" x1="270" y1="336" x2="270" y2="64" stroke="#ffffff" stroke-width="3" stroke-dasharray="14 12"/>
      <!-- branching road -->
      <path class="road-branch" d="M300,250 C330,190 400,120 500,68 L508,74 C420,130 360,200 338,262 Z" fill="var(--blue-soft)"/>
      <path class="road-branch-line" d="M320,252 C345,190 410,125 503,71" fill="none" stroke="var(--blue-deep)" stroke-width="3"/>
      <circle class="branch-point" cx="503" cy="71" r="6" fill="var(--blue-mid)"/>
    </svg>

    <p class="subtitle">How people experience life<br>from the inside out</p>

    <p class="authors">Carl Whitby <span class="conjunction">and</span> Martin Holloway</p>
  </main>
</body>
</html>
```